Online-Marketing Material für Autohaus mit Werkstätten
Zielgruppe
Wir betreiben ein Autohaus mit Werkstätte und suchen hierfür Auszubildende in folgenden Berufen:
Kfz-Mechatroniker, Automobilkaufmann, Fachkraft für Lagerlogistik.
Aufgabenstellung
Die Post sollen Jugendliche ansprechen und sich an dem bisherigen Layout orientieren.

```html
<!DOCTYPE html>
<html lang="de">
<head>
<meta charset="utf-8">
<title>Ausbildung im Autohaus Kestner</title>
<link rel="stylesheet" href="https://fonts.googleapis.com/css2?family=Roboto:wght@400;700;900&family=Montserrat:wght@700&display=swap">
<style>
  :root {
    --navy: #1c2b6c;
    --ink: #111111;
    --ink-soft: #2a2a2a;
    --accent: #f2e600;
    --white: #ffffff;
    --bg-light: #f3f4f6;
    --bg-mid: #d9dde2;
    --shirt: #7f97bf;
    --shirt-dark: #5c74a0;
    --hair: #3a2a26;
  }
  * { box-sizing: border-box; margin: 0; padding: 0; }
  html, body { width: 1200px; height: 1200px; overflow: hidden; }
  body { font-family: "Roboto", Arial, sans-serif; color: var(--ink); }

  .post {
    position: relative;
    width: 1200px;
    height: 1200px;
    overflow: hidden;
    background:
      radial-gradient(ellipse 520px 420px at 360px 330px, #c9ced4 0%, rgba(201,206,212,0) 70%),
      linear-gradient(180deg, var(--bg-light) 0%, var(--bg-mid) 55%, #eef0f2 100%);
  }
  .post__scene {
    position: absolute;
    inset: 0;
    background: linear-gradient(90deg, rgba(255,255,255,0.55) 0%, rgba(255,255,255,0.15) 60%, rgba(255,255,255,0) 100%);
  }
  .post__person {
    position: absolute;
    left: 640px;
    top: 0;
    width: 560px;
    height: 1200px;
    border-radius: 240px 240px 0 0;
    background: linear-gradient(180deg, var(--hair) 0%, #6b5a55 26%, var(--shirt) 40%, var(--shirt-dark) 80%, #3e4f6e 100%);
    opacity: 0.9;
  }

  .brand {
    position: absolute;
    left: 111px;
    top: 118px;
    display: flex;
    align-items: center;
    gap: 12px;
    font-family: "Roboto", Arial, sans-serif;
    font-weight: 700;
    font-size: 34px;
    letter-spacing: 0.5px;
    color: var(--ink-soft);
  }
  .brand__mark {
    width: 16px;
    height: 16px;
    border-radius: 50%;
    background: var(--ink-soft);
  }

  .eyebrow {
    position: absolute;
    left: 114px;
    top: 336px;
    font-size: 25px;
    font-weight: 400;
    letter-spacing: 2px;
    color: var(--ink-soft);
  }

  .headline {
    position: absolute;
    left: 108px;
    top: 400px;
    font-size: 88px;
    font-weight: 900;
    line-height: 85px;
    letter-spacing: 1px;
    color: var(--ink);
    text-transform: uppercase;
  }
  .headline__slash {
    display: inline-block;
    width: 22px;
    height: 40px;
    margin-left: 26px;
    background: var(--accent);
    transform: skewX(-22deg);
    vertical-align: baseline;
  }

  .jobs {
    position: absolute;
    left: 111px;
    top: 694px;
    list-style: none;
    font-size: 44px;
    font-weight: 400;
    line-height: 64px;
    color: var(--ink);
  }

  .cta {
    position: absolute;
    left: 111px;
    top: 914px;
    width: 539px;
    height: 83px;
    border-radius: 42px;
    background: var(--navy);
    color: var(--white);
    font-family: "Montserrat", Arial, sans-serif;
    font-weight: 700;
    font-size: 29px;
    letter-spacing: 1px;
    display: flex;
    align-items: center;
    justify-content: center;
    padding-right: 26px;
    text-decoration: none;
  }

  .contact {
    position: absolute;
    top: 1091px;
    display: flex;
    align-items: center;
    gap: 18px;
    font-size: 26px;
    color: var(--ink);
  }
  .contact--web { left: 111px; }
  .contact--mail { left: 589px; }
  .contact__icon {
    width: 54px;
    height: 54px;
    border-radius: 50%;
    background: var(--navy);
    border: 3px solid #c9d0e6;
    display: flex;
    align-items: center;
    justify-content: center;
  }

  .chevrons {
    position: absolute;
    left: 1024px;
    top: 1100px;
  }
</style>
</head>
<body>
  <main class="post">
    <div class="post__scene" role="img" aria-label="Unscharfer Hintergrund: Autohaus mit hellem Fahrzeug"></div>
    <div class="post__person" role="img" aria-label="Lächelnde junge Frau im blauen Hemd mit verschränkten Armen"></div>

    <div class="brand"><span class="brand__mark"></span>Autohaus Kestner</div>

    <p class="eyebrow">AUSBILDUNG</p>

    <h1 class="headline">
      Lust auf<br>
      eine Ausbildung<br>
      bei uns?<span class="headline__slash"></span>
    </h1>

    <ul class="jobs">
      <li>KFZ-Mechatroniker (m/w/d) /</li>
      <li>Automobilkaufmann (m/w/d) /</li>
      <li>Fachkraft für Lagerlogistik (m/w/d)</li>
    </ul>

    <a class="cta" href="#">JETZT BEWERBEN !</a>

    <div class="contact contact--web">
      <span class="contact__icon">
        <svg width="30" height="30" viewBox="0 0 30 30" fill="none" stroke="#ffffff" stroke-width="2">
          <circle cx="15" cy="15" r="12"/>
          <ellipse cx="15" cy="15" rx="5.5" ry="12"/>
          <line x1="3" y1="15" x2="27" y2="15"/>
          <line x1="5" y1="9" x2="25" y2="9"/>
          <line x1="5" y1="21" x2="25" y2="21"/>
        </svg>
      </span>
      <span>www.karriere-kestnerhaus.de</span>
    </div>

    <div class="contact contact--mail">
      <span class="contact__icon">
        <svg width="28" height="22" viewBox="0 0 28 22" fill="none" stroke="#ffffff" stroke-width="2">
          <rect x="2" y="2" width="24" height="18" rx="2"/>
          <polyline points="2,3 14,12 26,3"/>
        </svg>
      </span>
      <span>ausbildung@kestnerhaus.de</span>
    </div>

    <svg class="chevrons" width="70" height="36" viewBox="0 0 70 36" fill="none" stroke="#f2e600" stroke-width="3">
      <polyline points="4,4 16,18 4,32"/>
      <polyline points="27,4 39,18 27,32"/>
      <polyline points="50,4 62,18 50,32"/>
    </svg>
  </main>
</body>
</html>
```